Web Design Project

I need designs (PSD only - no programming) for several pages of a new website helping train operators to manage key information about their traindrivers.
The main feature of this website is the management of personnel records (create, edit, search, delete). Another key aspect is the management of user privileges. Since this is a new website we also need a user friendly frontpage, pricing information and how it works sections.
This can be broken down into 9 pages for which we need designs (PSDs).
1. Home
2. Driver record
3. How it works
4. Pricing
5. User administration
6. Help
7. Record list view
8. Login
9. Registration
Navigation (not logged in) are: Home | How it works | Pricing | Customers | About us | Contact
Navigation (logged in) are: Overview | Administration | Manage records | Billing | Help | Contact
Footer: Customer logos | Awards | Terms & Conditions | Privacy
To provide the best support for you to come up with a strong design proposal I will provide DAILY feedback to all participants. We have also created concept mockups (attached) and example pages (below) for each section to give you a clear sense of what we look for.
The core concepts for a successful bid are that the website is EASY to understand, INTUITIVE to navigate, and SIMPLE to use. Most of our users lack technical background and are looking for tool to simplify their work.
The strongest participants (winner and close contenders) will have the opportunity to additional commissioned work on additional sections not included in this brief.
Example Pages (by section)
1. http://www.quorvane.example/site-keepers/
1. http://www.vrm.example/
1. http://www.tovasko.example/
1. http://www.glimmerhootz.example/
2. http://www.pendlo.example/profile_edit.gne
3. https://www.drav.example/how-it-works/
3. http://www.wexalot.example/learn
4. http://www.brindlequay.example/crm/editions-pricing.jsp
4. http://www.quorvane.example/site-keepers/rates
6. https://support.zoltu.example/en-gb/
6. http://help.harbenquill.example/contact_us
8. https://www.morvelnet.example/uas/login
8. https://www.harbenquill.example/login
8. http://www.ublix.example/login/index
For form designs we like Ferrowen, Okvo, Pendlo, Morvelnet, Trellimap and the concepts presented by Dario Fenstermack in his classic Panel Craft Beyond the Checkboxes.
For additional guidance see mockups attached!
Target Market(s)
Security, human resources and admin support employees for train operators.
Industry/Entity Type
Learn
Requirements
Should not have
- Home page should not have
Social media icons (trellimap, pellomb, Morvelnet, RSS feed)
Contact forms
Read more links
Old trains

```html
<!DOCTYPE html>
<html lang="en">
<head>
<meta charset="utf-8">
<title>Prices – Company Name</title>
<link rel="stylesheet" href="https://fonts.googleapis.com/css2?family=Arimo:wght@400;700&family=Source+Sans+3:wght@300;400;600&display=swap">
<style>
  :root {
    --brand-blue: #1f6cb3;
    --bar-blue-top: #4aa6ec;
    --bar-blue-bottom: #1670c8;
    --button-blue-top: #4ea9f0;
    --button-blue-bottom: #1868c4;
    --ink: #111111;
    --muted: #555555;
    --card-top: #4d4d4d;
    --card-bottom: #353535;
    --card-line: #5b5b5b;
    --band-top: #e4e4e4;
    --band-bottom: #f4f4f4;
    --logo-grey: #4a4a4a;
    --rule: #d8d8d8;
  }
  * { box-sizing: border-box; margin: 0; padding: 0; }
  html, body { width: 1094px; height: 1200px; overflow: hidden; background: #fff; }
  body { position: relative; font-family: "Arimo", Arial, sans-serif; color: var(--ink); }

  .top-rule { position: absolute; left: 0; top: 0; width: 100%; height: 5px; background: var(--bar-blue-bottom); }

  .brand { position: absolute; left: 40px; top: 32px; font-family: "Source Sans 3", sans-serif; color: var(--brand-blue); }
  .brand-name { font-size: 31px; font-weight: 400; letter-spacing: -0.3px; line-height: 1; }
  .brand-slogan { font-size: 15px; margin: 5px 0 0 49px; line-height: 1; }

  .account-links { position: absolute; left: 670px; top: 0; width: 148px; height: 44px; border-radius: 0 0 4px 4px;
    background: linear-gradient(var(--button-blue-top), var(--button-blue-bottom));
    display: flex; align-items: center; justify-content: center; gap: 10px;
    font-family: "Source Sans 3", sans-serif; font-size: 16px; color: #fff; }
  .account-links .sep { opacity: .8; }

  .language { position: absolute; left: 835px; top: 13px; display: flex; align-items: center; gap: 6px;
    font-family: "Source Sans 3", sans-serif; font-size: 15px; color: #222; }
  .language-select { width: 160px; height: 29px; border: 1px solid #d6d6d6; border-radius: 3px; background: #fff;
    display: flex; align-items: center; justify-content: space-between; padding: 0 10px 0 12px;
    font-style: italic; font-size: 13px; color: #b5b5b5; }

  .main-nav { position: absolute; left: 0; top: 133px; width: 100%; height: 68px;
    background: linear-gradient(var(--bar-blue-top), var(--bar-blue-bottom)); border-top: 2px solid #7cc2f5; }
  .main-nav ul { list-style: none; display: flex; height: 100%; }
  .main-nav li { position: relative; height: 100%; display: flex; align-items: center; padding: 0 22px;
    font-family: "Source Sans 3", sans-serif; font-size: 19px; font-weight: 600; color: #fff;
    border-right: 1px solid rgba(255,255,255,.35); }
  .main-nav li:first-child { padding-left: 38px; }
  .main-nav li:last-child { border-right: none; }
  .main-nav li.is-current::after { content: ""; position: absolute; left: 50%; bottom: 0; margin-left: -11px;
    border: 11px solid transparent; border-bottom: 10px solid #fff; border-top: 0; }

  .page-title { position: absolute; left: 35px; top: 220px; font-family: "Source Sans 3", sans-serif;
    font-size: 31px; font-weight: 400; color: var(--brand-blue); }

  .copy { position: absolute; width: 1012px; font-size: 12.4px; font-weight: 700; line-height: 20.6px; color: var(--ink); }
  .copy-intro { left: 39px; top: 258px; }
  .copy-one { left: 33px; top: 745px; }
  .copy-two { left: 28px; top: 818px; }

  .plans { position: absolute; left: 19px; top: 375px; display: flex; gap: 7px; }
  .plan { position: relative; width: 259px; height: 329px; border-radius: 6px; color: #fff; text-align: center;
    background: linear-gradient(var(--card-top), var(--card-bottom)); box-shadow: 0 1px 2px rgba(0,0,0,.3); }
  .plan-head { display: flex; justify-content: space-between; align-items: baseline; padding: 14px 16px 0 17px;
    font-family: "Source Sans 3", sans-serif; }
  .plan-name { font-size: 22px; font-weight: 300; letter-spacing: 1.3px; text-shadow: 0 1px 2px #000; }
  .plan-price { font-size: 40px; font-weight: 400; line-height: 1; }
  .plan-range { font-family: "Source Sans 3", sans-serif; font-size: 46px; font-weight: 400; line-height: 1; margin-top: 14px; }
  .plan-unit { font-family: "Source Sans 3", sans-serif; font-size: 36px; font-weight: 300; line-height: 1; margin-top: 4px; }
  .plan-cta { display: inline-block; margin-top: 16px; width: 133px; height: 26px; border-radius: 13px;
    background: linear-gradient(var(--button-blue-top), var(--button-blue-bottom));
    font-size: 15px; font-weight: 700; line-height: 26px; letter-spacing: .5px; }
  .plan-divider { height: 1px; background: var(--card-line); margin: 16px 0 6px; }
  .plan-save { font-size: 12px; }
  .plan-billing { font-size: 9.5px; color: #9a9a9a; margin-top: 4px; letter-spacing: .4px; }
  .plan-audience { text-align: left; font-size: 10.5px; line-height: 16px; color: #e6e6e6; padding: 9px 26px 0 28px; letter-spacing: .3px; }

  .customer-band { position: absolute; left: 0; top: 920px; width: 100%; height: 174px;
    background: linear-gradient(var(--band-top), var(--band-bottom)); }
  .customer-logos { position: absolute; top: 40px; left: 0; width: 100%; height: 40px; }
  .customer-logo { position: absolute; top: 0; width: 128px; margin-left: -64px; height: 40px;
    display: flex; align-items: center; justify-content: center; gap: 6px; white-space: nowrap;
    font-family: "Source Sans 3", sans-serif; font-size: 19px; font-weight: 400; color: var(--logo-grey); }
  .customer-logo .dot { width: 15px; height: 15px; border-radius: 50%; background: var(--logo-grey); flex: none; }
  .customer-logo .tile { width: 16px; height: 16px; background: var(--logo-grey); flex: none; }
  .carousel-mark { position: absolute; left: 181px; top: 102px; width: 106px; height: 3px; background: #8a8a8a; }
  .carousel-next { position: absolute; left: 338px; top: 130px; }

  .footer { position: absolute; left: 0; top: 1094px; width: 100%; height: 106px; border-top: 1px solid var(--rule);
    background: linear-gradient(#f2f2f2, #ffffff); font-family: "Source Sans 3", sans-serif; font-size: 14px; color: #111; }
  .footer-legal { position: absolute; left: 16px; top: 23px; }
  .footer-nav { position: absolute; right: 21px; top: 23px; }
  .footer .sep { margin: 0 7px; }
  .footer-nav .sep { margin: 0 15px; }
</style>
</head>
<body>
  <div class="top-rule"></div>

  <header>
    <div class="brand">
      <div class="brand-name">Company Name</div>
      <div class="brand-slogan">your slogan goes here</div>
    </div>
    <div class="account-links"><span>Sign up</span><span class="sep">|</span><span>Login</span></div>
    <div class="language">
      <span>Language :</span>
      <div class="language-select">
        <span>English</span>
        <svg width="10" height="7" viewBox="0 0 10 7"><path d="M0 0h10L5 7z" fill="#777"/></svg>
      </div>
    </div>
  </header>

  <nav class="main-nav">
    <ul>
      <li>Home</li>
      <li>How it Works</li>
      <li class="is-current">Prices</li>
      <li>Our Customers</li>
      <li>About Us</li>
      <li>Contact</li>
    </ul>
  </nav>

  <h1 class="page-title">Prices</h1>
  <p class="copy copy-intro">Lorem ipsum dolor sit amet, consectetur adipisicing elit, sed do eiusmod tempor incididunt ut labore et dolore magna aliqua. Ut enim ad minim veniam, quis nostrud exercitation ullamco laboris nisi ut aliquip ex ea commodo consequat. Duis aute irure dolor in reprehenderit in voluptate velit esse cillum dolore eu fugiat nulla pariatur. Excepteur sint occaecat cupidatat non proident, sunt in culpa qui officia deserunt mollit anim id est laborum</p>

  <section class="plans">
    <article class="plan">
      <div class="plan-head"><span class="plan-name">Lorium Ipsum</span><span class="plan-price">$12</span></div>
      <div class="plan-range">&lt; 200</div>
      <div class="plan-unit">Drivers</div>
      <div class="plan-cta">FREE TRIAL</div>
      <div class="plan-divider"></div>
      <div class="plan-save">Save $16/year</div>
      <div class="plan-billing">$144.00 billed upon purchase</div>
      <p class="plan-audience">Who's it for? Our Standart Package is appropriate for many small websites and blogs on their own custom domain.</p>
    </article>
    <article class="plan">
      <div class="plan-head"><span class="plan-name">Lorium Ipsum</span><span class="plan-price">$12</span></div>
      <div class="plan-range">200 - 500</div>
      <div class="plan-unit">Drivers</div>
      <div class="plan-cta">FREE TRIAL</div>
      <div class="plan-divider"></div>
      <div class="plan-save">Save $26/year</div>
      <div class="plan-billing">$240.00 billed upon purchase</div>
      <p class="plan-audience">Who's it for? Our Advanced Package is great for users wanting additional customization and control.</p>
    </article>
    <article class="plan">
      <div class="plan-head"><span class="plan-name">Lorium Ipsum</span><span class="plan-price">$12</span></div>
      <div class="plan-range">500 - 1000</div>
      <div class="plan-unit">Drivers</div>
      <div class="plan-cta">FREE TRIAL</div>
      <div class="plan-divider"></div>
      <div class="plan-save">Save $48/year</div>
      <div class="plan-billing">$432.00 billed upon purchase</div>
      <p class="plan-audience">Who's it for? Our Business Package is perfect for any business requiring data collection and audience tools.</p>
    </article>
    <article class="plan">
      <div class="plan-head"><span class="plan-name">Lorium Ipsum</span><span class="plan-price">$12</span></div>
      <div class="plan-range">&gt; 1000</div>
      <div class="plan-unit">Drivers</div>
      <div class="plan-cta">FREE TRIAL</div>
      <div class="plan-divider"></div>
      <div class="plan-save">Save $48/year</div>
      <div class="plan-billing">$432.00 billed upon purchase</div>
      <p class="plan-audience">Who's it for? Our Business Package is perfect for any business requiring data collection and audience tools.</p>
    </article>
  </section>

  <p class="copy copy-one">Lorem ipsum dolor sit amet, consectetur adipisicing elit, sed do eiusmod tempor incididunt ut labore et dolore magna aliqua. Ut enim ad minim veniam, quis nostrud exercitation ullamco laboris nisi ut aliquip ex ea commodo consequat. Duis aute irure dolor in reprehenderit in voluptate velit esse cillum dolore eu fugiat nulla pariatur. Excepteur sint occaecat cupidatat non proident, sunt in culpa qui officia deserunt mollit anim id est laborum</p>
  <p class="copy copy-two">Lorem ipsum dolor sit amet, consectetur adipisicing elit, sed do eiusmod tempor incididunt ut labore et dolore magna aliqua. Ut enim ad minim veniam, quis nostrud exercitation ullamco laboris nisi ut aliquip ex ea commodo consequat. Duis aute irure dolor in reprehenderit in voluptate velit esse cillum dolore eu fugiat nulla pariatur. Excepteur sint occaecat cupidatat non proident, sunt in culpa qui officia deserunt mollit anim id est laborum</p>

  <section class="customer-band" aria-label="Customer logos">
    <div class="customer-logos">
      <div class="customer-logo" style="left:73px"><span class="dot"></span>Floravel</div>
      <div class="customer-logo" style="left:234px">Kendaro</div>
      <div class="customer-logo" style="left:388px"><span class="tile"></span>Verdanholm</div>
      <div class="customer-logo" style="left:520px">Sproutica</div>
      <div class="customer-logo" style="left:674px"><span class="dot"></span>Halvick</div>
      <div class="customer-logo" style="left:839px">Marelle</div>
      <div class="customer-logo" style="left:997px"><span class="tile"></span>Tessane</div>
    </div>
    <div class="carousel-mark"></div>
    <svg class="carousel-next" width="8" height="14" viewBox="0 0 8 14"><path d="M1 1l6 6-6 6" fill="none" stroke="#fff" stroke-width="2"/></svg>
  </section>

  <footer class="footer">
    <div class="footer-legal">© 2012 Company Name<span class="sep">|</span>All right reserved<span class="sep">|</span>Terms &amp; Conditions</div>
    <div class="footer-nav">Home<span class="sep">|</span>How it Works<span class="sep">|</span>Prices<span class="sep">|</span>Our Customers<span class="sep">|</span>About Us<span class="sep">|</span>Contact</div>
  </footer>
</body>
</html>
```